New Meal Prep Flyer for New Package Deals

We are looking for a design that displays our new packages that we offer. If you take a look at our website www.copperspoonpantry.com, and click on packages , you'll see the way we display them currently . We would like something similar to that in style . The first package is called "Evergreen" and this package will be a 1 week package (7 days ), 2 meals a day, for a price of $195.00. The second package is called "Pebble" and this package will be a 3 week package (21 days) 2 meals per day, for a price of $546.00 , the third package is a 6 week+ package (45 days), and it is called "Lighthouse" , 2 meals per day , and the price is $1080.00 .
For the Pebble Package , can you put next to it "Save $42.00!"
For the Lighthouse Package, can you put next to it "Save $180!"
We also want our logo on the flyer (see attached), and we are just looking for a 1 page flyer , 8 1/2 x 11.

```html
<!DOCTYPE html>
<html lang="en">
<head>
<meta charset="utf-8">
<title>Copper Spoon Pantry – New Packages Flyer</title>
<link rel="stylesheet" href="https://fonts.googleapis.com/css2?family=Montserrat:wght@500;600;700;800&family=Oswald:wght@500;600&display=swap">
<style>
  :root {
    --page-bg: #ececec;
    --white: #ffffff;
    --green: #8cc21f;
    --green-deep: #6a9d17;
    --green-strip: #5f8f18;
    --grey: #6f7072;
    --grey-deep: #58595b;
    --grey-strip: #4f5052;
    --orange: #f5a012;
    --orange-deep: #e27a0c;
    --orange-strip: #cf640e;
    --logo-grey: #707173;
    --photo-top: #d9dcc8;
    --photo-mid: #c4cfa6;
    --wood-light: #b88a63;
    --wood-dark: #8a6444;
  }
  * { box-sizing: border-box; margin: 0; padding: 0; }
  html, body { width: 1200px; height: 1200px; overflow: hidden; }
  body { background: var(--page-bg); font-family: "Montserrat", Arial, sans-serif; position: relative; }

  .flyer { position: absolute; left: 160px; top: 30px; width: 880px; height: 1140px; overflow: hidden; background: var(--white); }

  .backdrop { position: absolute; left: 0; top: 220px; width: 880px; height: 860px;
    background: linear-gradient(180deg, var(--photo-top) 0%, var(--photo-mid) 35%, #d8d6c0 62%, var(--wood-light) 74%, var(--wood-dark) 100%); }

  .header-wave, .footer-wave { position: absolute; left: 0; display: block; }
  .header-wave { top: 0; }
  .footer-wave { top: 930px; }

  .brand { position: absolute; left: 24px; top: 32px; }
  .brand-name { display: flex; align-items: center; gap: 9px; font-weight: 800; font-size: 35px; color: var(--logo-grey); letter-spacing: 0.5px; line-height: 1; }
  .brand-dot { width: 16px; height: 16px; border-radius: 50%; background: var(--green); }
  .brand-tagline { margin-top: 12px; font-weight: 700; font-size: 18px; color: var(--green); letter-spacing: 0.3px; }

  .headline { position: absolute; left: 500px; top: 50px; width: 340px; text-align: center; color: var(--white); font-weight: 700; line-height: 1.05; text-shadow: 0 3px 6px rgba(0,0,0,0.25); }
  .headline-top { display: block; font-size: 82px; }
  .headline-bottom { display: block; font-size: 70px; }

  .package { position: absolute; top: 455px; width: 272px; height: 441px; }
  .package-strip { position: absolute; left: 0; top: 90px; width: 48px; height: 351px; border-radius: 40px 0 0 0; }
  .package-strip span { position: absolute; left: 50%; bottom: 16px; transform-origin: left bottom; transform: rotate(-90deg) translate(0, 50%); white-space: nowrap; color: var(--white); font-weight: 700; font-size: 22px; letter-spacing: 1px; text-transform: uppercase; }
  .package-card { position: absolute; left: 46px; top: 0; width: 226px; height: 441px; background: var(--white); border-radius: 44px 0 0 0; }
  .package-price { position: absolute; right: 14px; top: 10px; font-family: "Oswald", "Arial Narrow", sans-serif; font-weight: 600; font-size: 50px; line-height: 1; }
  .package-price small { font-size: 24px; }
  .package-body { position: absolute; left: 0; top: 71px; width: 226px; height: 370px; border-radius: 56px 0 56px 0; text-align: center; color: var(--white); font-weight: 600; font-size: 22px; line-height: 1.32; padding-top: 94px; }
  .package-term { display: inline-block; background: var(--white); font-weight: 700; font-size: 27px; padding: 3px 14px; margin-bottom: 14px; }
  .package-meals { margin-top: 32px; }

  .package-evergreen { left: 24px; }
  .package-evergreen .package-strip { background: var(--green-strip); }
  .package-evergreen .package-price, .package-evergreen .package-term { color: var(--green-deep); }
  .package-evergreen .package-body { background: linear-gradient(160deg, var(--green) 0%, var(--green-deep) 100%); }

  .package-pebble { left: 309px; }
  .package-pebble .package-strip { background: var(--grey-strip); }
  .package-pebble .package-price, .package-pebble .package-term { color: var(--grey-deep); }
  .package-pebble .package-body { background: linear-gradient(160deg, var(--grey) 0%, var(--grey-deep) 100%); }

  .package-lighthouse { left: 594px; }
  .package-lighthouse .package-strip { background: var(--orange-strip); }
  .package-lighthouse .package-price, .package-lighthouse .package-term { color: var(--orange-deep); }
  .package-lighthouse .package-body { background: linear-gradient(160deg, var(--orange) 0%, var(--orange-deep) 100%); }

  .savings { position: absolute; top: 379px; width: 148px; height: 54px; border-radius: 22px 22px 0 22px; color: var(--white); font-weight: 600; font-size: 17px; line-height: 1.2; text-align: center; padding-top: 6px; }
  .savings-pebble { left: 423px; background: var(--grey); }
  .savings-lighthouse { left: 703px; background: var(--orange); }

  .store-badges { position: absolute; left: 115px; top: 960px; }
  .store-badge { width: 170px; height: 45px; border-radius: 7px; margin-bottom: 12px; }
  .store-badge-dark { background: #2b2b2b; }
  .store-badge-light { background: var(--white); border: 2px solid #bdbdbd; }
  .image-credit { font-size: 9px; font-weight: 600; color: #7a7a7a; text-align: center; width: 170px; line-height: 1.2; }

  .contact { position: absolute; left: 430px; top: 1036px; width: 430px; text-align: center; color: var(--white); }
  .contact-icon { display: block; margin: 0 auto 10px; }
  .contact-web { font-weight: 700; font-size: 29px; letter-spacing: 0.2px; white-space: nowrap; }
</style>
</head>
<body>
<main class="flyer">
  <div class="backdrop" role="img" aria-label="Softly blurred garden terrace background with a wooden tabletop in the foreground"></div>

  <svg class="header-wave" width="880" height="380" viewBox="0 0 880 380" aria-hidden="true">
    <path d="M0,0 H880 V300 C720,345 560,270 380,250 C230,234 110,262 0,318 Z" fill="var(--white)"/>
    <path d="M420,0 H880 V282 C720,320 560,262 390,236 C250,216 120,236 0,292 V262 C110,200 230,196 320,150 C390,110 400,40 420,0 Z" fill="var(--green)"/>
    <path d="M0,292 C120,236 250,216 390,236 C560,262 720,320 880,282 V300 C720,345 560,278 390,252 C250,232 120,250 0,306 Z" fill="#dcdcdc"/>
  </svg>

  <div class="brand">
    <div class="brand-name"><span class="brand-dot"></span>COPPER SPOON</div>
    <div class="brand-tagline">HEALTHY KITCHEN &nbsp;|&nbsp; MEAL PREP</div>
  </div>

  <h1 class="headline"><span class="headline-top">NEW</span><span class="headline-bottom">Packages</span></h1>

  <div class="savings savings-pebble">Save<br>$42.00!</div>
  <div class="savings savings-lighthouse">Save<br>$180.00!</div>

  <section class="package package-evergreen">
    <div class="package-strip"><span>★ Evergreen ★</span></div>
    <div class="package-card">
      <div class="package-price">$195<small>.00</small></div>
      <div class="package-body">
        <div class="package-term">1 WEEK</div>
        <div>package<br>(7 days )</div>
        <div class="package-meals">2 meals<br>a day</div>
      </div>
    </div>
  </section>

  <section class="package package-pebble">
    <div class="package-strip"><span>★ Pebble ★</span></div>
    <div class="package-card">
      <div class="package-price">$546<small>.00</small></div>
      <div class="package-body">
        <div class="package-term">3 WEEK</div>
        <div>package<br>(21 days )</div>
        <div class="package-meals">2 meals<br>a day</div>
      </div>
    </div>
  </section>

  <section class="package package-lighthouse">
    <div class="package-strip"><span>★ Lighthouse ★</span></div>
    <div class="package-card">
      <div class="package-price">$1080<small>.00</small></div>
      <div class="package-body">
        <div class="package-term">6+ WEEK</div>
        <div>package<br>(45 days )</div>
        <div class="package-meals">2 meals<br>a day</div>
      </div>
    </div>
  </section>

  <svg class="footer-wave" width="880" height="210" viewBox="0 0 880 210" aria-hidden="true">
    <path d="M0,120 C280,40 580,10 880,0 V210 H0 Z" fill="var(--white)"/>
    <path d="M0,148 C290,80 580,48 880,36 V210 H0 Z" fill="var(--green)"/>
  </svg>

  <div class="store-badges">
    <div class="store-badge store-badge-dark"></div>
    <div class="store-badge store-badge-light"></div>
    <div class="image-credit">BACKGROUND FROM<br>STOCKLEAF.COM</div>
  </div>

  <div class="contact">
    <svg class="contact-icon" width="48" height="48" viewBox="0 0 48 48" aria-hidden="true">
      <circle cx="24" cy="24" r="23" fill="var(--white)"/>
      <path d="M17 13 l5 6 -3 3 c2 4 4 6 8 8 l3 -3 6 5 -3 4 c-10 0 -19 -9 -19 -19 z" fill="var(--green)"/>
      <path d="M27 14 a8 8 0 0 1 7 7 M27 10 a12 12 0 0 1 11 11" stroke="var(--green)" stroke-width="2" fill="none" stroke-linecap="round"/>
    </svg>
    <div class="contact-web">copperspoonpantry.com</div>
  </div>
</main>
</body>
</html>
```